Business Card Design for Music Therapy Startup

I began my journey attending the Brantwell College School of Music to become a music educator before changing my degree and graduating with a Bachelor's degree in Music with an Outside Field in Psychology in 2008. From there, I attended Pelham Ridge University where I completed my Bachelor's Equivalency degree in Music Therapy. I became a Board Certified - Music Therapist almost 3 years ago and have since specialized in geriatrics, bereavement and end of life care. I anticipate completing my Master's Degree in Music Therapy in May, 2015, from Quarry Hollow University.

In August of 2014 I completed advanced training in Neurologic Music Therapy (NMT) allowing me to also address speech and language, sensorimotor and cognitive deficits which develop as a result of neurologic injury and disease processes. Parkinson's Disease, Stroke, Traumatic Brain Injury and Dementia are amongst some of the neurologic conditions which may be treated with NMT.

My Philosophy: I strive to provide professional, genuine and compassionate care to all individuals, families and facilities that I serve. I use evidence-based and standardized music-based therapeutic techniques to achieve results which are documented, while complying with privacy regulations. I work with my patients and families to assess the primary goals to be addressed and to establish the most effective treatment plan to facilitate the best results.

Danielle R. Osterby, MT-BC
Neurologic Music Therapist

Willowbrook Music Therapy, LLC

472.906.1543

www.willowbrookmusictherapy.example
willowbrookNMT@mailbox.example

```html
<!DOCTYPE html>
<html lang="en">
<head>
<meta charset="utf-8">
<title>Willowbrook Music Therapy, LLC – Business Card</title>
<link rel="stylesheet" href="https://fonts.googleapis.com/css2?family=Exo+2:wght@400;500&display=swap">
<style>
  :root {
    --page-bg: #e6e6e8;
    --card-bg: #fbfbfc;
    --brand-blue: #5b8fd2;
    --divider-grey: #a9a9ab;
    --shadow: rgba(0, 0, 0, 0.12);
  }
  * { box-sizing: border-box; margin: 0; padding: 0; }
  html, body {
    width: 1200px;
    height: 864px;
    overflow: hidden;
    background: var(--page-bg);
    font-family: "Exo 2", "Trebuchet MS", sans-serif;
  }
  .canvas {
    width: 1200px;
    height: 864px;
    display: flex;
    align-items: center;
    justify-content: center;
  }
  .business-card {
    position: relative;
    width: 1000px;
    height: 572px;
    background: var(--card-bg);
    box-shadow: 0 10px 30px var(--shadow);
    color: var(--brand-blue);
  }
  .brand {
    position: absolute;
    top: 160px;
    left: 0;
    right: 0;
    display: flex;
    align-items: center;
    justify-content: center;
    gap: 20px;
  }
  .brand-mark {
    width: 26px;
    height: 26px;
    border-radius: 50%;
    background: var(--brand-blue);
  }
  .brand-name {
    font-size: 56px;
    font-weight: 500;
    letter-spacing: 0.2px;
  }
  .contact-block {
    position: absolute;
    top: 330px;
    left: 0;
    right: 0;
    display: flex;
    justify-content: center;
    align-items: stretch;
  }
  .person {
    display: flex;
    flex-direction: column;
    justify-content: center;
    align-items: flex-end;
    padding-right: 24px;
  }
  .person-name {
    font-size: 31px;
    font-weight: 400;
    line-height: 1.15;
  }
  .person-title {
    font-size: 17px;
    font-weight: 400;
    margin-top: 2px;
  }
  .divider {
    width: 2px;
    height: 118px;
    background: var(--divider-grey);
  }
  .contact-list {
    list-style: none;
    padding-left: 26px;
    display: flex;
    flex-direction: column;
    justify-content: center;
    gap: 8px;
  }
  .contact-item {
    display: flex;
    align-items: center;
    gap: 18px;
    font-size: 20px;
  }
  .contact-icon {
    width: 22px;
    height: 22px;
    flex: none;
  }
</style>
</head>
<body>
  <main class="canvas">
    <section class="business-card">
      <div class="brand">
        <span class="brand-mark" aria-hidden="true"></span>
        <span class="brand-name">Willowbrook Music Therapy, LLC</span>
      </div>

      <div class="contact-block">
        <div class="person">
          <p class="person-name">Danielle R. Osterby</p>
          <p class="person-title">MT-BC Neurologic Music Therapist</p>
        </div>
        <div class="divider" aria-hidden="true"></div>
        <ul class="contact-list">
          <li class="contact-item">
            <svg class="contact-icon" viewBox="0 0 24 24" aria-hidden="true">
              <path fill="#5b8fd2" d="M3 8c0-2 4-4 9-4s9 2 9 4v2h-5V8.5c-1-.6-2.5-.8-4-.8s-3 .2-4 .8V10H3z"/>
              <path fill="#5b8fd2" d="M7 11h10l2 8H5z"/>
              <circle cx="12" cy="15" r="2" fill="#fbfbfc"/>
            </svg>
            <span>472.906.1543</span>
          </li>
          <li class="contact-item">
            <svg class="contact-icon" viewBox="0 0 24 24" aria-hidden="true">
              <rect x="2" y="5" width="20" height="14" fill="#5b8fd2"/>
              <path d="M2 5l10 8 10-8" fill="none" stroke="#fbfbfc" stroke-width="1.6"/>
            </svg>
            <span>www.willowbrookmusictherapy.example</span>
          </li>
          <li class="contact-item">
            <svg class="contact-icon" viewBox="0 0 24 24" aria-hidden="true">
              <rect x="3" y="4" width="18" height="12" fill="none" stroke="#5b8fd2" stroke-width="2"/>
              <rect x="10" y="16" width="4" height="3" fill="#5b8fd2"/>
              <rect x="7" y="19" width="10" height="2" fill="#5b8fd2"/>
            </svg>
            <span>willowbrookNMT@mailbox.example</span>
          </li>
        </ul>
      </div>
    </section>
  </main>
</body>
</html>
```